Fern Tower AG – The secret mission

Hi all. We would love to enhance our website and the sales funnel like on our website www.ferntower.ch
We are looking for a clean and fresh design which is reflecting our
two main passions: "gaming and investing".
For infos pls have a look at the website www.ferntower.ch, our youtube channel.
You find many info attached. We are curious how you interprete the topic.

Target Market(s)

Gamers | Investor - worldwide market

Industry/Entity Type

Games

Number of Pages Required

5+ page

Requirements
Must have
• 6 Sites, fresh and modern design (gaming)
Nice to have
• sales funnel (Get involved page) in the same design, webshop
Should not have
• Our shares are on a blockchain, which are very modern (www.plimex.ch). So blockchain design is okay but please no affiliation to bitcoin or crytpocurrencies. thx.

```html
<!DOCTYPE html>
<html lang="en">
<head>
<meta charset="utf-8">
<title>Fern Tower AG – Gaming and Investing</title>
<link rel="stylesheet" href="https://fonts.googleapis.com/css2?family=Open+Sans:wght@400;600;700&display=swap">
<style>
:root{
  --red:#e31e24;
  --red-dark:#c8161c;
  --black:#000;
  --footer:#111;
  --navy:#071c36;
  --navy-mid:#0d3a6e;
  --blue-glow:#1a7ad6;
  --teal:#3fd1d6;
  --ink:#222;
  --text:#444;
  --light:#f4f5f7;
  --white:#fff;
}
*{margin:0;padding:0;box-sizing:border-box}
html,body{width:1200px;height:4167px;overflow:hidden}
body{position:relative;font-family:"Open Sans",Arial,sans-serif;color:var(--text);background:var(--white)}
.abs{position:absolute}

/* hero */
.hero{left:0;top:0;width:1200px;height:700px;background:var(--black);overflow:hidden}
.hero-art{left:200px;top:280px;width:800px;height:420px;background:radial-gradient(ellipse at 50% 45%,#4fb6d8 0%,#1d5a7a 30%,#0a1c28 60%,#000 80%)}
.brand{left:175px;top:48px;display:flex;align-items:center;gap:10px}
.brand-dot{width:40px;height:40px;border-radius:50%;background:var(--red)}
.brand-name{font-size:17px;font-weight:600;color:var(--red)}
.nav{right:170px;top:60px;display:flex;gap:14px}
.nav a{color:var(--white);font-size:14px;text-decoration:none;font-weight:400}
.hero-title{left:0;width:1200px;top:172px;text-align:center;color:var(--white);font-size:48px;font-weight:600;letter-spacing:.5px}
.hero-sub{left:0;width:1200px;top:242px;text-align:center;color:var(--white);font-size:32px;font-weight:400}
.zigzag{left:0;top:660px;width:1200px;height:40px}

/* buttons */
.btn{display:inline-flex;align-items:center;justify-content:center;background:var(--red);color:var(--white);font-weight:700;font-size:15px;border-radius:5px;text-transform:uppercase}

/* about */
.section-title{font-size:33px;font-weight:700;color:var(--red)}
.about-title{left:173px;top:810px}
.about-text{left:173px;top:872px;width:480px;font-size:12.3px;line-height:22.5px;color:#333}
.about-btn{left:173px;top:1080px;width:131px;height:54px}
.about-ring{left:674px;top:774px;width:372px;height:380px}
.about-art{left:695px;top:797px;width:334px;height:334px;border-radius:50%;background:radial-gradient(circle at 50% 45%,#4c8fa2 0%,#1f4f63 45%,#0a2634 100%)}

/* involve */
.involve{left:0;top:1248px;width:1200px;height:625px;background:linear-gradient(120deg,#fff 0%,#f1f3f6 50%,#e9ecf0 100%)}
.form-card{left:173px;top:1336px;width:304px;height:453px;background:var(--red);border-radius:6px;box-shadow:0 6px 18px rgba(0,0,0,.25)}
.form-card h3{position:absolute;left:0;top:24px;width:304px;text-align:center;color:var(--white);font-size:24px;font-weight:600;line-height:32px}
.field{position:absolute;height:52px;background:var(--white);border-radius:4px;font-size:15px;color:#555;padding:0 10px;display:flex;align-items:center}
.field.select{justify-content:space-between}
.submit{left:8px;top:368px;width:140px;height:53px;background:var(--red-dark);border-radius:4px}
.involve-title{left:548px;top:1370px}
.involve-text{left:548px;top:1428px;width:480px;font-size:12.3px;line-height:22.5px;color:#333}
.involve-text p{margin-bottom:14px}
.involve-btn{left:548px;top:1688px;width:131px;height:56px}

/* faq */
.faq{left:0;top:1873px;width:1200px;height:597px;background:radial-gradient(ellipse at 60% 0%,var(--blue-glow) 0%,var(--navy-mid) 35%,var(--navy) 75%)}
.faq-title{left:173px;top:1990px;font-size:33px;font-weight:600;color:var(--white)}
.faq-item{left:173px;width:450px;height:53px;background:var(--white);border-radius:4px;display:flex;align-items:center;justify-content:space-between;padding:0 8px 0 14px;font-size:15px;font-weight:600;color:#222}
.plus{width:40px;height:40px;background:var(--red);border-radius:4px;display:flex;align-items:center;justify-content:center}
.faq-art{left:744px;top:1989px;width:404px;height:372px;background:radial-gradient(ellipse at 50% 50%,rgba(63,209,214,.55) 0%,rgba(30,120,150,.3) 40%,rgba(7,28,54,0) 72%)}

/* posts */
.posts-title{left:0;width:1200px;top:2548px;text-align:center;font-size:33px;font-weight:600;color:var(--red)}
.post{top:2641px;width:419px;height:263px;border:1.5px solid #9a9a9a;border-radius:6px;background:var(--white)}
.post-img{position:absolute;left:6px;top:6px;width:170px;height:249px;border-radius:3px}
.post h4{position:absolute;left:188px;top:20px;width:218px;font-size:14.5px;font-weight:600;color:#222;line-height:23px;text-align:justify}
.post p{position:absolute;left:188px;top:106px;width:218px;font-size:10.5px;line-height:22.5px;color:#444;text-align:justify}

/* content types */
.types-title{left:0;width:1200px;top:3012px;text-align:center;font-size:25px;font-weight:400;color:#222;line-height:36px}
.tile{top:3124px;width:270px;height:364px}
.tile-title{top:3506px;width:270px;text-align:center;font-size:21px;font-weight:600;color:#222}
.tile-text{top:3550px;width:270px;text-align:center;font-size:11.7px;line-height:20px;color:#444}

/* footer */
.footer{left:0;top:3703px;width:1200px;height:464px;background:var(--footer)}
.footer-brand{left:0;width:1200px;top:3788px;display:flex;flex-direction:column;align-items:center;gap:14px}
.footer-dot{width:60px;height:60px;border-radius:50%;background:var(--white)}
.footer-name{font-size:24px;font-weight:600;color:var(--white)}
.footer-nav{left:0;width:1200px;top:4000px;text-align:center;font-size:16px;color:var(--white)}
.footer-nav span{margin:0 10px}
.footer-rule{left:173px;top:4072px;width:854px;height:1px;background:#cfcfcf}
.copyright{left:0;width:1200px;top:4106px;text-align:center;font-size:15px;color:var(--white)}
</style>
</head>
<body>

<!-- hero -->
<div class="abs hero">
  <div class="abs hero-art" role="img" aria-label="Hand holding glowing interconnected wireframe cubes"></div>
  <div class="abs brand"><span class="brand-dot"></span><span class="brand-name">Fern Tower AG</span></div>
  <nav class="abs nav"><a>HOME</a><a>ABOUT US</a><a>GET INVOLVED</a><a>FAQ</a><a>PRESS</a><a>CONTACT US</a></nav>
  <h1 class="abs hero-title">GAMING AND INVESTING</h1>
  <p class="abs hero-sub">FinTech in Gaming</p>
</div>
<svg class="abs zigzag" viewBox="0 0 1200 40" preserveAspectRatio="none">
  <polygon fill="#fff" points="0,40 0,35 60,10 110,30 180,5 250,28 320,8 390,30 450,12 520,32 600,6 680,30 740,10 820,30 890,8 960,28 1030,6 1100,30 1150,10 1200,28 1200,40"/>
</svg>

<!-- about -->
<h2 class="abs section-title about-title">ABOUT US</h2>
<p class="abs about-text">Fern Tower AG is a Swiss holding company, investing in the booming online videogame sector. Our main focus centres on the gaming community. Our highest priority is the Plavex software – the First International Play Money Exchange. Plavex has developed a next-generation disruptive virtual asset exchange to help online video game players easily and securely value and trade their in-game virtual money, items and services between games worlds or for cash. This will bring the real-world and virtual economies closer together. Gamers will have the opportunity to make money with, and from, their passion in videogames.</p>
<div class="abs btn about-btn">Read More</div>
<svg class="abs about-ring" viewBox="0 0 372 380">
  <path d="M186 6 A180 182 0 1 1 30 96" fill="none" stroke="#e31e24" stroke-width="7" stroke-linecap="round"/>
</svg>
<div class="abs about-art" role="img" aria-label="Glowing wireframe cube above a digital grid"></div>

<!-- get involved -->
<div class="abs involve"></div>
<div class="abs form-card">
  <h3>BECOME A<br>SHAREHOLDER:</h3>
  <div class="field" style="left:8px;top:116px;width:288px">Email Address</div>
  <div class="field" style="left:8px;top:176px;width:140px">First Name</div>
  <div class="field" style="left:155px;top:176px;width:141px">First Name</div>
  <div class="field" style="left:8px;top:236px;width:288px">Country</div>
  <div class="field select" style="left:8px;top:298px;width:288px"><span>Quantity of Shares (€5 each)</span><span style="font-size:11px">▼</span></div>
  <div class="abs btn submit">Submit Now</div>
</div>
<h2 class="abs section-title involve-title">GET INVOLVED</h2>
<div class="abs involve-text">
  <p>Own a part of the future of gaming – pledge your support and take an ownership stake as we drive forward the launch of Plavex, and other pojects in the future!</p>
  <p>Plavex has just finished a two year development sprint, the product is ready and Fern Tower is selling shares to raise the final money needed to fund the worldwide launch and the development of the trading ecosystem. We firmly believe Plavex is going to be huge!</p>
  <p>You can get involved and help make this happen by buying shares in our private share sale. Our shares are tokenized blockchain shares issued by Plimex.ch, the digital share platform for Swiss SME powered by Alpnet.</p>
</div>
<div class="abs btn involve-btn">Read More</div>

<!-- faq -->
<div class="abs faq"></div>
<h2 class="abs faq-title">FREQUENTLY ASKED QUESTIONS</h2>
<div class="abs faq-item" style="top:2067px">What are tokenised shares?<span class="plus"><svg width="18" height="18" viewBox="0 0 18 18"><path d="M9 2v14M2 9h14" stroke="#fff" stroke-width="2.5"/></svg></span></div>
<div class="abs faq-item" style="top:2135px">What is the link betwen Plavex<span class="plus"><svg width="18" height="18" viewBox="0 0 18 18"><path d="M9 2v14M2 9h14" stroke="#fff" stroke-width="2.5"/></svg></span></div>
<div class="abs faq-item" style="top:2203px">What is Plavex?<span class="plus"><svg width="18" height="18" viewBox="0 0 18 18"><path d="M9 2v14M2 9h14" stroke="#fff" stroke-width="2.5"/></svg></span></div>
<div class="abs faq-item" style="top:2270px">What is Fern Tower AG<span class="plus"><svg width="18" height="18" viewBox="0 0 18 18"><path d="M9 2v14M2 9h14" stroke="#fff" stroke-width="2.5"/></svg></span></div>
<div class="abs faq-art" role="img" aria-label="Four glowing teal wireframe cubes"></div>

<!-- recent posts -->
<h2 class="abs posts-title">RECENT POSTS</h2>
<article class="abs post" style="left:173px">
  <div class="post-img" role="img" aria-label="Colourful isometric block lettering artwork" style="background:linear-gradient(135deg,#3a2a6e,#6b3fa0 40%,#d8a21e 75%,#2b2b3a)"></div>
  <h4>The History and the Team Behind Plavex: Interview with Founders, Part 1</h4>
  <p>Plavex was founded in 2017 by Lukas Brenner and Jonas Weiler who both devoted their lives to commodity trading and gaming and lately decided to put all their effort into merging the best of these two worlds at the Plavex exchange.</p>
</article>
<article class="abs post" style="left:608px">
  <div class="post-img" role="img" aria-label="Gamer at a dimly lit desk with glowing screens" style="background:linear-gradient(160deg,#1a1a22,#2a3850 45%,#8a2a1e 80%,#140e0e)"></div>
  <h4>The Ingame Items Market is Broken… But Here's How it Can Be Fixed</h4>
  <p>Today, we are all used to quality service wherever we go and whatever products we use. And it seems illogical to us that most ingame items trading platforms are so com plicated to use and so inefficient regarding how users transact.</p>
</article>

<!-- content types -->
<h2 class="abs types-title">What Types of Downloadable Ingame Content Are There and<br>Why Do We Buy Them?</h2>
<div class="abs tile" style="left:173px;background:linear-gradient(90deg,#3c4a58 0%,#6f7c88 25%,#eeeeee 30%,#f4f4f4 100%)" role="img" aria-label="Game covers beside an infographic of content packs"></div>
<div class="abs tile" style="left:466px;background:linear-gradient(170deg,#b84a1a 0%,#7a2a20 35%,#2c3b7a 70%,#141a3a 100%)" role="img" aria-label="Fantasy strategy game box art"></div>
<div class="abs tile" style="left:757px;background:linear-gradient(160deg,#2a3a26 0%,#6e7a3a 40%,#8a8a7a 70%,#3a3a36 100%)" role="img" aria-label="Armoured horse in a game scene"></div>
<h3 class="abs tile-title" style="left:173px">Nova Wars: Frontline</h3>
<h3 class="abs tile-title" style="left:466px">Sugar Swap Bank</h3>
<h3 class="abs tile-title" style="left:757px">Realmcraft II</h3>
<p class="abs tile-text" style="left:173px">In fact, many contemporary F2P games give you just enough free content to make you start liking the game.</p>
<p class="abs tile-text" style="left:466px">Armor, weapons, vehicles and other stuff that increases your ingame strength and takes your overall performance to a higher level.</p>
<p class="abs tile-text" style="left:757px">Boost and cheats this DLC unlocks game parts which are usually only earned by playing the game.</p>

<!-- footer -->
<footer class="abs footer"></footer>
<div class="abs footer-brand"><span class="footer-dot"></span><span class="footer-name">Fern Tower AG</span></div>
<nav class="abs footer-nav">HOME<span>|</span>ABOUT US<span>|</span>GET INVOLVED<span>|</span>FAQ<span>|</span>PRESS<span>|</span>CONTACT US</nav>
<div class="abs footer-rule"></div>
<p class="abs copyright">Copyrights @ 2021 Fern Tower AG. All Rights Reserved.</p>

</body>
</html>
```